Bold Website Redesign for a Disruptive Training Brand

Brightmoor Labs is a bold, no-fluff sales & leadership training company powered by AI-driven practice and behavioral science. We’ve already built our website structure and copy in Craftly.io — now we need a designer to fully transform the visual design across all pages (Home, Approach, Programs, About, Contact).
We’re looking for a modern, memorable, high-performance aesthetic that blends human energy, science, and tech without feeling corporate or safe. Clean, bold typography, fluid layout, strong emotional hero moments, subtle motion, and imagery that mixes real people with abstract scientific/tech visuals.Because our clients are primarily North American, please ensure any human photography or AI-generated imagery reflects a North American business context and demographics (modern, diverse, and realistic).

Your job is visual redesign only — no coding required.
The final design must be practical to rebuild inside Craftly.io.

A full, detailed creative brief (plus logo files) is included in the uploaded files.
If you can bring a mix of edge, intelligence, and strong visual storytelling, we’d love to see your work.

Website is already built in Craftly.io at - https://brightmoor-website-tempdesign.craftly.app — structure is set, visuals need redesign.

```html
<!DOCTYPE html>
<html lang="en">
<head>
<meta charset="utf-8">
<title>Brightmoor Labs — Training That Practices Back</title>
<link href="https://fonts.googleapis.com/css2?family=IBM+Plex+Sans:wght@300;400;700&family=Roboto:wght@400;500;700&display=swap" rel="stylesheet">
<style>
:root{
  --navy:#0f1f3d;
  --navy-2:#182a4a;
  --ink:#0f1f3d;
  --blue:#3a63b8;
  --sky:#3ec6ee;
  --mid:#3f8ad6;
  --grey-bg:#f4f5f7;
  --field:#f2f3f5;
  --text:#2b2f36;
  --muted:#8a8f98;
}
*{box-sizing:border-box;margin:0;padding:0}
html,body{width:1200px;height:3270px;overflow:hidden}
body{position:relative;font-family:"Roboto",Arial,sans-serif;color:var(--text);background:#fff}
.abs{position:absolute}
.heading{font-family:"IBM Plex Sans",Arial,sans-serif;font-weight:300;color:var(--ink);text-transform:uppercase;line-height:1.2}
.heading b{font-weight:700}
.rule{display:block;width:70px;height:2px;background:var(--mid)}
.btn{position:absolute;display:flex;align-items:center;justify-content:center;gap:8px;font-weight:700;font-size:14px;text-transform:uppercase;color:#fff;background:linear-gradient(90deg,var(--blue),var(--sky));border-radius:3px}
.social{display:flex;gap:26px}
.social span{width:20px;height:20px;border-radius:50%;background:currentColor;opacity:.7}

/* top bar */
.topbar{left:0;top:0;width:1200px;height:48px;background:var(--navy);color:#fff;font-size:14.5px}
.topbar .item{position:absolute;top:15px;display:flex;align-items:center;gap:8px}
.topbar .talk{left:934px;top:3px;width:121px;height:42px;font-size:13px}

/* nav */
.nav{left:0;top:48px;width:1200px;height:110px;background:#fff;border-bottom:1px solid #eee}
.brand{position:absolute;display:flex;align-items:center;gap:10px;font-family:"Roboto",Arial,sans-serif;font-weight:700;letter-spacing:3px;text-transform:uppercase}
.nav .brand{left:145px;top:42px;font-size:16px;color:var(--ink)}
.brand i{display:block;width:22px;height:22px;border-radius:50%;background:var(--mid);flex:none}
.menu{position:absolute;left:397px;top:0;height:110px;display:flex;font-size:15.5px;font-weight:500;color:var(--ink)}
.menu a{display:flex;align-items:center;padding:0 19px;text-decoration:none;color:inherit}
.menu a.active{background:#f2f3f5;color:var(--mid)}
.nav .divider{left:940px;top:30px;width:1px;height:52px;background:#ccc}
.nav .social{position:absolute;left:980px;top:45px;color:#777}

/* hero */
.hero{left:0;top:158px;width:1200px;height:600px}
.hero-photo{position:absolute;inset:0;background:linear-gradient(100deg,#0d2f6e 0%,#1a3f86 35%,#2a3550 60%,#6a5a58 85%,#c08a70 100%);clip-path:polygon(0 0,100% 0,100% 528px,600px 600px,0 483px)}
.hero-accent{position:absolute;inset:0;background:linear-gradient(90deg,#3a7bdc,#1c3f96);clip-path:polygon(0 420px,600px 600px,0 483px);opacity:.9}
.hero h1{position:absolute;left:144px;top:125px;font-family:"IBM Plex Sans",Arial,sans-serif;color:#fff;font-weight:300;font-size:44px;line-height:1.17;text-transform:uppercase}
.hero h1 b{font-weight:700;font-size:46px}
.hero p{position:absolute;left:144px;top:234px;width:520px;color:#fff;font-size:21.5px;line-height:1.5;font-weight:500}
.hero .b1{left:144px;top:350px;width:174px;height:44px}
.hero .b2{left:325px;top:350px;width:173px;height:44px;background:#fff;color:var(--mid)}

/* problem */
.problem{left:0;top:758px;width:1200px;height:452px;background:var(--grey-bg);text-align:center}
.problem .heading{position:absolute;left:0;width:1200px;top:100px;font-size:39px}
.problem .rule{position:absolute;left:565px;top:197px}
.problem p{position:absolute;left:176px;width:848px;top:222px;font-size:19.5px;line-height:1.5;color:#2b2f36}
.problem .link{position:absolute;left:0;width:1200px;top:332px;font-size:20px;color:var(--blue)}

/* team */
.team{left:0;top:1210px;width:1200px;height:510px;background:#fff}
.team .visual{position:absolute;left:145px;top:30px;width:445px;height:480px;background:linear-gradient(160deg,#dfe8f6,#8fb6e6 60%,#3a63b8);border-radius:4px}
.team .heading{position:absolute;left:631px;top:100px;font-size:33px}
.team .rule{position:absolute;left:631px;top:222px}
.team p{position:absolute;left:631px;top:248px;width:425px;font-size:15px;line-height:1.6}
.team .btn{left:631px;top:371px;width:157px;height:44px}

/* practice */
.practice{left:0;top:1720px;width:1200px;height:553px;background:linear-gradient(110deg,#3a63b8 0%,#3f8ad6 55%,#3ec6ee 100%);text-align:center;color:#fff}
.practice .heading{position:absolute;left:0;width:1200px;top:65px;font-size:40px;color:#fff}
.practice .rule{position:absolute;left:563px;top:115px;background:#fff}
.practice .sub{position:absolute;left:0;width:1200px;top:138px;font-size:20px;font-weight:500}
.card{position:absolute;top:198px;width:288px;height:280px;background:#fff;border-radius:26px;color:var(--text)}
.card .icon{position:absolute;left:101px;top:38px;width:86px;height:86px;border-radius:50%;background:#e8eef8;display:flex;align-items:center;justify-content:center}
.card h3{position:absolute;left:0;width:100%;top:143px;font-size:20px;font-weight:500;color:var(--ink)}
.card p{position:absolute;left:20px;width:248px;top:176px;font-size:15px;line-height:1.6}

/* contact */
.contact{left:0;top:2273px;width:1200px;height:680px;background:#fff}
.contact .decor{position:absolute;left:0;top:0;width:300px;height:680px;background:linear-gradient(160deg,#c9dfa6 0%,#eef2f4 30%,#e4e7ec 60%,#fff 100%)}
.contact .left-h{position:absolute;left:144px;top:116px;font-size:33px}
.contact .left-rule{position:absolute;left:144px;top:234px}
.contact .lead{position:absolute;left:144px;top:264px;width:410px;font-size:15px;line-height:1.6}
.info{position:absolute;left:144px;display:flex;gap:14px;font-size:14.5px;line-height:1.45}
.info .dot{width:44px;height:44px;border-radius:50%;background:linear-gradient(135deg,var(--blue),var(--sky));display:flex;align-items:center;justify-content:center;flex:none}
.info strong{display:block;font-weight:500;color:var(--ink)}
.contact .left-social{position:absolute;left:144px;top:540px;color:#777}
.contact .right-h{position:absolute;left:599px;top:117px;font-size:33px}
.contact .right-rule{position:absolute;left:599px;top:162px}
.contact .right-lead{position:absolute;left:599px;top:190px;width:420px;font-size:15px;line-height:1.6}
.field{position:absolute;left:599px;width:456px;height:44px;background:var(--field);border-radius:4px;padding:14px 17px;font-size:14.5px;font-style:italic;color:var(--muted)}
.contact .send{left:599px;top:524px;width:456px;height:46px}

/* footer */
.footer{left:0;top:2953px;width:1200px;height:262px;background:var(--navy);color:#fff}
.footer .brand{left:145px;top:88px;width:210px;flex-direction:column;gap:12px;font-size:22px;line-height:1.15;color:#fff;letter-spacing:4px;text-align:center}
.footer .brand i{width:40px;height:40px}
.fcol{position:absolute;top:68px;font-size:13px}
.fcol h4{font-size:15px;font-weight:500;text-transform:uppercase;margin-bottom:6px}
.fcol .rule{width:38px;margin-bottom:18px;background:var(--sky)}
.fcol li{list-style:none;height:29px}
.fcol .ci{display:flex;gap:14px;align-items:flex-start;height:42px;line-height:1.5}
.fcol .ci .dot{width:24px;height:24px;border-radius:50%;background:#1f3a6e;flex:none}
.sub-field{position:absolute;left:836px;top:102px;width:220px;height:33px;background:#fff;border-radius:17px;overflow:hidden;display:flex;align-items:center;font-size:10px;color:#444;padding-left:16px}
.sub-field .go{position:absolute;right:0;top:0;width:45px;height:33px;background:linear-gradient(90deg,var(--mid),var(--sky))}
.bottombar{left:0;top:3215px;width:1200px;height:55px;background:var(--navy-2);color:#fff;font-size:12px}
.bottombar .copy{position:absolute;left:0;width:1200px;top:20px;text-align:center}
.bottombar .social{position:absolute;left:996px;top:18px;color:#8a97b0}
</style>
</head>
<body>

<header class="abs topbar">
  <div class="item" style="left:505px">
    <svg width="13" height="13" viewBox="0 0 24 24" fill="#3ec6ee"><path d="M6.6 10.8a15.1 15.1 0 0 0 6.6 6.6l2.2-2.2a1 1 0 0 1 1-.25 11.4 11.4 0 0 0 3.6.57 1 1 0 0 1 1 1V20a1 1 0 0 1-1 1A17 17 0 0 1 3 4a1 1 0 0 1 1-1h3.5a1 1 0 0 1 1 1c0 1.25.2 2.45.57 3.57a1 1 0 0 1-.25 1z"/></svg>
    +1 (480) 555-0142
  </div>
  <div class="item" style="left:677px">
    <svg width="14" height="12" viewBox="0 0 24 20" fill="none" stroke="#3ec6ee" stroke-width="2"><rect x="1" y="1" width="22" height="18" rx="2"/><path d="M1 3l11 8 11-8"/></svg>
    hello@brightmoorlabs.com
  </div>
  <div class="btn talk">
    <svg width="14" height="12" viewBox="0 0 24 20" fill="#fff"><path d="M2 2h14a2 2 0 0 1 2 2v6a2 2 0 0 1-2 2H8l-4 4v-4H2a2 2 0 0 1-2-2V4a2 2 0 0 1 2-2z"/></svg>
    Let's Talk
  </div>
</header>

<nav class="abs nav">
  <div class="brand"><i></i>Brightmoor Labs</div>
  <div class="menu">
    <a class="active">HOME</a><a>APPROACH</a><a>PROGRAMS</a><a>ABOUT</a><a>CONTACT</a>
  </div>
  <div class="abs divider"></div>
  <div class="social" aria-label="Social links"><span></span><span></span></div>
</nav>

<section class="abs hero">
  <div class="hero-photo" role="img" aria-label="Photo of a business team reviewing data on a glowing tech interface, blended with abstract blue circuitry"></div>
  <div class="hero-accent"></div>
  <h1>Training that<br><b>practices back</b></h1>
  <p>You'll see measurable growth as your people turn insight into habit — automatically, sustainably, and without extra work for their leaders.</p>
  <div class="btn b1">See how we do it</div>
  <div class="btn b2">
    <svg width="14" height="12" viewBox="0 0 24 20" fill="#3f8ad6"><path d="M2 2h14a2 2 0 0 1 2 2v6a2 2 0 0 1-2 2H8l-4 4v-4H2a2 2 0 0 1-2-2V4a2 2 0 0 1 2-2z"/></svg>
    Let's Talk
  </div>
</section>

<section class="abs problem">
  <h2 class="heading">The real problem isn't your people —<br>it's the <b>forgetting curve</b></h2>
  <span class="rule"></span>
  <p>Within a week, most training disappears. Leaders are left guessing who's using what they learned — and no one has time to fix it. We built Brightmoor Labs to make progress automatic, measurable, and real.</p>
  <div class="link">Watch how sustained practice changes the curve ⟶</div>
</section>

<section class="abs team">
  <div class="visual" role="img" aria-label="Photo of a smiling woman sitting cross-legged with a laptop, framed by blue stripes"></div>
  <h2 class="heading">Built by people who've<br>led the <b>change<br>themselves</b></h2>
  <span class="rule"></span>
  <p>Behind Brightmoor Labs are leaders who've lived the challenge of making learning last. They've scaled companies, built cultures, and led transformation — and now they've designed the system they always wished existed.</p>
  <div class="btn">Meet the team</div>
</section>

<section class="abs practice">
  <h2 class="heading">Practice made <b>permanent</b></h2>
  <span class="rule"></span>
  <div class="sub">You'll replace "hope they remember" with a system that makes sure they do.</div>

  <div class="card" style="left:145px">
    <div class="icon"><svg width="44" height="44" viewBox="0 0 44 44" fill="none" stroke="#3a63b8" stroke-width="2"><circle cx="22" cy="20" r="12"/><circle cx="22" cy="20" r="4"/><path d="M16 32v8M28 32v8"/></svg></div>
    <h3>LEARN</h3>
    <p>Fast, focused workshops, built on science, that install the mindset and skills that matter most.</p>
  </div>
  <div class="card" style="left:456px">
    <div class="icon"><svg width="40" height="44" viewBox="0 0 40 44" fill="none" stroke="#3a63b8" stroke-width="2"><rect x="6" y="4" width="26" height="34" rx="2"/><path d="M12 13h14M12 19h14M12 25h9"/><circle cx="30" cy="32" r="5"/></svg></div>
    <h3>CERTIFY</h3>
    <p>Programmatic AI-driven practice and feedback - mastery without management overhead.</p>
  </div>
  <div class="card" style="left:768px">
    <div class="icon"><svg width="44" height="44" viewBox="0 0 44 44" fill="none" stroke="#3a63b8" stroke-width="2"><circle cx="22" cy="22" r="16"/><circle cx="22" cy="18" r="4"/><circle cx="13" cy="21" r="3"/><circle cx="31" cy="21" r="3"/><path d="M15 30c2-5 12-5 14 0"/></svg></div>
    <h3>SUSTAIN</h3>
    <p>Light-touch challenges and dashboards that keep skills sharp long after training ends.</p>
  </div>
</section>

<section class="abs contact">
  <div class="decor" role="img" aria-label="Soft photo of a green plant and a laptop corner on a white desk"></div>
  <h2 class="heading left-h">Ready to see what<br>lasting <b>capability<br>looks like?</b></h2>
  <span class="rule left-rule"></span>
  <p class="lead">Reach out through any of these channels, and we'll respond quickly to start the conversation.</p>
  <div class="info" style="top:333px">
    <span class="dot"><svg width="14" height="14" viewBox="0 0 24 24" fill="#fff"><path d="M6.6 10.8a15.1 15.1 0 0 0 6.6 6.6l2.2-2.2a1 1 0 0 1 1-.25 11.4 11.4 0 0 0 3.6.57 1 1 0 0 1 1 1V20a1 1 0 0 1-1 1A17 17 0 0 1 3 4a1 1 0 0 1 1-1h3.5a1 1 0 0 1 1 1c0 1.25.2 2.45.57 3.57a1 1 0 0 1-.25 1z"/></svg></span>
    <div><strong>Phone:</strong>hello@brightmoorlabs.net</div>
  </div>
  <div class="info" style="top:389px">
    <span class="dot"><svg width="15" height="12" viewBox="0 0 24 20" fill="none" stroke="#fff" stroke-width="2.5"><rect x="1" y="1" width="22" height="18" rx="2"/><path d="M1 3l11 8 11-8"/></svg></span>
    <div><strong>Email:</strong>hello@brightmoorlabs.net</div>
  </div>
  <div class="info" style="top:445px">
    <span class="dot"><svg width="12" height="15" viewBox="0 0 16 22" fill="#fff"><path d="M8 0a8 8 0 0 1 8 8c0 6-8 14-8 14S0 14 0 8a8 8 0 0 1 8-8zm0 5a3 3 0 1 0 0 6 3 3 0 0 0 0-6z"/></svg></span>
    <div><strong>Address:</strong>4820 E Canyon Ridge Rd Suite 210<br>Tempe, AZ 85281</div>
  </div>
  <div class="social left-social" aria-label="Social links"><span></span><span></span></div>

  <h2 class="heading right-h">Get in <b>touch</b></h2>
  <span class="rule right-rule"></span>
  <p class="right-lead">Lasting growth starts with one — a real conversation about what's working, what's not, and what's possible.</p>
  <div class="field" style="top:252px">Name</div>
  <div class="field" style="top:306px">Organization</div>
  <div class="field" style="top:359px">Email</div>
  <div class="field" style="top:413px;height:100px">Message</div>
  <div class="btn send">Send message</div>
</section>

<footer class="abs footer">
  <div class="brand"><i></i><span>Brightmoor<br>Labs</span></div>
  <div class="fcol" style="left:423px">
    <h4>Site Map</h4><span class="rule"></span>
    <ul><li>Home</li><li>Approach</li><li>Programs</li><li>About</li><li>Contact</li></ul>
  </div>
  <div class="fcol" style="left:582px">
    <h4>Contact Info</h4><span class="rule"></span>
    <div class="ci"><span class="dot"></span>+1 (480) 555-0142</div>
    <div class="ci"><span class="dot"></span>hello@brightmoorlabs.com</div>
    <div class="ci"><span class="dot"></span>4820 E Canyon Ridge Rd Suite 210<br>Tempe, AZ 85281</div>
  </div>
  <div class="fcol" style="left:835px">
    <h4>Subscribe</h4><span class="rule"></span>
  </div>
  <div class="sub-field">Email Address<span class="go"></span></div>
</footer>

<div class="abs bottombar">
  <div class="copy">© 2025 &nbsp;/&nbsp; All Rights Reserved</div>
  <div class="social" aria-label="Social links"><span></span><span></span></div>
</div>

</body>
</html>
```